ASSET BASED PROGRAM FLIER

Need flier to market hard money loan products offered HARD MONEY FIX & FLIP PROGRAMS

We offer a variety of loan programs Some program highlights include......

1) No Minimum Credit Score
2) 3-5 Day Close
3) Up to 100% of Purchase & Rehab
4) Rates as Low as 7%
5) Loans Offered Nationwide

Contact us today for more information at (800) 647-2915 x42 or email us at mwelton@brightlanefunding.example NMLS #731856 www.brightlanefunding.example

```html
<!DOCTYPE html>
<html lang="en">
<head>
<meta charset="UTF-8">
<title>Hard Money Fix &amp; Flip Programs – Brightlane Funding</title>
<link rel="stylesheet" href="https://fonts.googleapis.com/css2?family=Arvo&family=Oswald:wght@300;400&family=Open+Sans:wght@400;600&display=swap">
<style>
  :root {
    --gold: #a8992c;
    --gold-light: #f3ecc8;
    --blue: #1c58a8;
    --ink: #3b3b3b;
    --paper: #ffffff;
    --backdrop: #e9e9e9;
    --hat: #f1c233;
  }
  * { box-sizing: border-box; margin: 0; padding: 0; }
  html, body { width: 1200px; height: 1200px; overflow: hidden; }
  body { background: var(--backdrop); position: relative; font-family: "Open Sans", sans-serif; }

  .flier {
    position: absolute; left: 214px; top: 54px;
    width: 772px; height: 1092px;
    background: var(--paper);
    overflow: hidden;
  }

  .brand {
    position: absolute; left: 44px; top: 58px;
    display: flex; align-items: center; gap: 12px;
  }
  .brand-dot { width: 34px; height: 34px; border-radius: 50%; background: var(--gold); }
  .brand-name { font-family: "Arvo", serif; font-size: 21px; color: var(--blue); line-height: 1.2; width: 200px; }

  .headline {
    position: absolute; left: 318px; top: 36px;
    font-family: "Arvo", serif; font-weight: 400;
    font-size: 41px; line-height: 52px; letter-spacing: 0.5px;
  }
  .headline .line-gold { color: var(--gold); display: block; }
  .headline .line-blue { color: var(--blue); display: block; }

  .hero-photo {
    position: absolute; left: 0; top: 167px; width: 772px; height: 433px;
    background: linear-gradient(120deg, #dcd6cc 0%, #efece6 45%, #c9a57a 80%, #b48a5a 100%);
  }

  .programs-band {
    position: absolute; left: 0; top: 600px; width: 772px; height: 35px;
    background: var(--gold); color: var(--gold-light);
    font-family: "Arvo", serif; font-size: 23.5px; line-height: 35px;
    text-align: center; letter-spacing: 0.3px;
  }

  .highlights {
    position: absolute; left: 0; top: 635px; width: 772px; height: 373px;
    background: var(--paper);
  }
  .highlights .side-strip {
    position: absolute; left: 0; top: 0; width: 70px; height: 100%;
    background: var(--blue);
  }
  .worker-photo {
    position: absolute; left: 342px; top: 59px; width: 430px; height: 314px;
    background:
      linear-gradient(90deg, var(--paper) 0%, rgba(255,255,255,0) 38%),
      linear-gradient(180deg, var(--paper) 0%, #f6eed8 22%, #e9d3c4 55%, #b9827c 82%, #9c5a58 100%);
  }
  .highlight-list { list-style: none; position: absolute; left: 46px; top: 32px; }
  .highlight-list li {
    display: flex; align-items: center; height: 61px;
    font-family: "Oswald", sans-serif; font-weight: 400; font-size: 20px; color: var(--ink);
  }
  .highlight-list .num {
    width: 46px; height: 46px; border-radius: 50%;
    background: var(--gold); border: 3px solid var(--paper);
    box-shadow: 0 0 0 1px #d8d8d8;
    color: var(--paper); font-size: 26px; font-weight: 300;
    display: flex; align-items: center; justify-content: center;
    margin-right: 13px;
  }

  .contact-band {
    position: absolute; left: 0; top: 1008px; width: 772px; height: 34px;
    background: var(--blue); color: var(--paper);
    display: flex; align-items: center; padding-left: 95px;
    font-family: "Open Sans", sans-serif; font-weight: 600; font-size: 15.5px; letter-spacing: -0.3px;
  }
  .contact-band .phone {
    font-family: "Oswald", sans-serif; font-weight: 400; font-size: 20px;
    color: var(--hat); margin-left: 12px;
  }

  .footer-band {
    position: absolute; left: 0; top: 1042px; width: 772px; height: 50px;
    background: var(--gold); color: var(--paper);
    display: flex; align-items: center; justify-content: center; gap: 14px;
    font-size: 15px;
  }
  .footer-band .item { display: flex; align-items: center; gap: 7px; }
  .footer-band svg { width: 17px; height: 17px; }
  .footer-band .divider { width: 1px; height: 28px; background: var(--gold-light); opacity: 0.7; }
  .footer-band .nmls { font-size: 12px; }
</style>
</head>
<body>
  <main class="flier">
    <header>
      <div class="brand">
        <span class="brand-dot"></span>
        <span class="brand-name">Brightlane Funding, Inc.</span>
      </div>
      <h1 class="headline">
        <span class="line-gold">HARD MONEY FIX</span>
        <span class="line-blue">&amp; FLIP PROGRAMS</span>
      </h1>
    </header>

    <div class="hero-photo" role="img" aria-label="Photo of a businesswoman and a contractor in a hard hat reviewing a clipboard inside a bright kitchen under renovation, with a sketched ladder and plant"></div>

    <div class="programs-band">WE OFFER A VARIETY OF LOAN PROGRAMS</div>

    <section class="highlights">
      <div class="side-strip"></div>
      <div class="worker-photo" role="img" aria-label="Photo of a smiling construction worker in a yellow hard hat and plaid shirt carrying lumber on his shoulder"></div>
      <ol class="highlight-list">
        <li><span class="num">1</span>No Minimum Credit Score</li>
        <li><span class="num">2</span>3-5 Day Close</li>
        <li><span class="num">3</span>Up to 100% of Purchase &amp; Rehab</li>
        <li><span class="num">4</span>Rates as Low as 7%</li>
        <li><span class="num">5</span>Loans Offered Nationwide</li>
      </ol>
    </section>

    <div class="contact-band">CONTACT US TODAY FOR MORE INFORMATION AT <span class="phone">(800) 647-2915 x42</span></div>

    <footer class="footer-band">
      <span class="item">
        <svg viewBox="0 0 20 20" fill="none" stroke="currentColor" stroke-width="1.5"><rect x="2" y="4" width="16" height="12"/><path d="M2 4l8 7 8-7M2 16l6-6M18 16l-6-6"/></svg>
        mwelton@brightlanefunding.example
      </span>
      <span class="item">
        <svg viewBox="0 0 20 20" fill="none" stroke="currentColor" stroke-width="1.3"><circle cx="10" cy="10" r="8"/><ellipse cx="10" cy="10" rx="3.5" ry="8"/><path d="M2 10h16M3.5 6h13M3.5 14h13"/></svg>
        www.brightlanefunding.example
      </span>
      <span class="divider"></span>
      <span class="nmls">NMLS #731856</span>
    </footer>
  </main>
</body>
</html>
```